car site and logo design

I am looking for a clean website that is easy to navigate to view and post used cars for sale. The required tabs are [Buy - Sell - News - Care Tips - Finance - Insurance - FAQ]
motorlane.example has a great search tool on the landing page. New & Zip code are not required.
wexa autos has a nice simple results display, although I am open to other neat clean layouts.
Users can create an account or login using their pinloop accounts, and follow, like, comment on other users posted cars. sellers can be given ratings as well.
displaying car information should be neat and simple, showing the seller name which can be clicked on and takes the viewer to the seller page to view other cars for sale if any. included in the car information when viewing a specific car a bell curve showing the prices available for the same car being sold on the site, and the position of this particular car.
the care tips, finance and insurance pages will have rectangular boxes with sponsored ads by the related companies.
the logo should be a cartoon style mechanic character, with a slogan next to it [buying a ride?, selling a ride?, ride adive? Query Tobin ] - the site will be called querytobin.
Sell tab would include a quick post box where user inserts the vehicle VIN number and will open a page where user will just have to upload the remaining data such as mileage, color, etc.
this is basically what the site is about.

Target Market(s)

target market will be older generation looking to buy and sell a car, will require easy features, as well as younger crowd who are familiar with using extra features.

Industry/Entity Type

Finance

Requirements
Nice to have
• site should have a light sense of social media site where user has a profile photo, can view user's history and activity

```html
<!DOCTYPE html>
<html lang="en">
<head>
<meta charset="utf-8">
<title>Query Tobin – Used Cars</title>
<link rel="stylesheet" href="https://fonts.googleapis.com/css2?family=Source+Sans+3:wght@300;400;600;700&display=swap">
<style>
:root{
  --ink:#2b2b2b;
  --muted:#8a8a8a;
  --topbar:#343434;
  --brand-blue:#1a3aa8;
  --link-blue:#1b3a9c;
  --form-blue:#1431c4;
  --field-blue:#0d24a0;
  --tab-dark:#0a2380;
  --orange:#f7921e;
  --orange-dark:#e7740a;
  --panel:#f1f1f1;
  --panel-line:#dedede;
  --footer:#efefef;
  --white:#ffffff;
}
*{box-sizing:border-box;margin:0;padding:0}
html,body{width:1200px;height:2546px;overflow:hidden}
body{position:relative;background:var(--white);font-family:"Source Sans 3",Arial,sans-serif;color:var(--ink)}
.abs{position:absolute}

/* top bar */
.topbar{left:0;top:0;width:1200px;height:46px;background:var(--topbar)}
.topbar .search{left:740px;top:11px;width:240px;height:26px;background:#262626;border-radius:2px;color:#666;font-size:13px;padding:4px 10px}
.topbar .search svg{position:absolute;right:8px;top:6px}
.topbar .auth{left:992px;top:13px;color:var(--white);font-size:13px;font-weight:700;letter-spacing:.3px}

/* header */
.header{left:0;top:46px;width:1200px;height:104px;background:linear-gradient(#fdfdfd,#e9e9e9)}
.logo{left:140px;top:12px}
.logo .mark{position:absolute;left:0;top:8px;width:44px;height:44px;border-radius:50%;background:var(--brand-blue)}
.logo .name{position:absolute;left:54px;top:4px;font-size:44px;font-weight:700;color:var(--ink);white-space:nowrap;line-height:1}
.logo .slogan{position:absolute;left:2px;top:70px;font-size:11px;color:var(--ink);white-space:nowrap}
.nav{left:506px;top:38px;display:flex;gap:0}
.nav a{font-size:19px;font-weight:600;color:#333;text-decoration:none;margin-right:33px}
.nav a.active{color:var(--link-blue);font-weight:700}

/* hero */
.hero{left:0;top:150px;width:1200px;height:548px;background:linear-gradient(100deg,#5b6168 0%,#8a9097 30%,#6f757b 55%,#b04a1e 75%,#5a5f66 100%)}
.hero .tagline{left:134px;top:32px;font-size:26px;font-weight:300;color:#e8e8e8}
.hero .arrow{width:56px;height:56px;border-radius:50%;background:rgba(255,255,255,.85)}
.tabs{left:134px;top:76px;display:flex}
.tab{height:58px;color:var(--white);font-size:19px;font-weight:700;display:flex;align-items:center;justify-content:center}
.tab.used{width:150px;background:var(--form-blue)}
.tab.cpo{width:205px;background:var(--tab-dark);margin-left:4px}
.search-form{left:134px;top:134px;width:394px;height:385px;background:var(--form-blue)}
.field{position:absolute;left:17px;width:357px;height:56px;background:var(--field-blue);color:#4f66c8;font-size:15px;padding:17px 14px}
.field .caret{position:absolute;right:14px;top:20px;width:17px;height:16px;background:#e8e8e8;border-radius:2px}
.field .caret::after{content:"";position:absolute;left:4px;top:5px;border:4px solid transparent;border-top:5px solid #333}
.field.miles{width:187px}
.btn-download{position:absolute;left:221px;top:261px;width:155px;height:54px;background:linear-gradient(var(--orange),var(--orange-dark));color:var(--white);font-size:20px;font-weight:600;display:flex;align-items:center;justify-content:center;border-radius:2px}
.search-form .links{position:absolute;top:346px;font-size:15px;color:var(--white)}

/* panels */
.panel{background:var(--panel);border:1px solid var(--panel-line)}
.panel-title{font-size:20px;color:var(--link-blue)}
.pager{font-size:20px;color:#222;font-weight:700;letter-spacing:4px}
.thumb{position:absolute;width:170px;height:151px;background:var(--white);border:1px solid #ddd;box-shadow:0 2px 4px rgba(0,0,0,.25);padding:6px}
.thumb .ph{width:100%;height:100%}
.cat-label{position:absolute;font-size:12px;color:#333}

.dealer{left:789px;top:727px;width:282px;height:268px}
.dealer .lbl{position:absolute;left:17px;font-size:13px;color:#444}
.dealer .input{position:absolute;left:17px;width:249px;height:42px;background:var(--white);border:1px solid #e3e3e3;color:#aaa;font-size:12px;padding:13px 10px}
.btn-orange{background:linear-gradient(var(--orange),var(--orange-dark));color:var(--white);font-weight:700;display:flex;align-items:center;justify-content:center;border-radius:2px}

.section-head{font-size:20px;font-weight:700;color:#222}

.filter{height:41px;background:#f3f3f3;border:1px solid #ddd;color:#999;font-size:14px;padding:11px 12px}
.filter .caret{position:absolute;right:10px;top:12px;width:16px;height:15px;border:1px solid #aaa;background:#fafafa}
.filter .caret::after{content:"";position:absolute;left:3px;top:5px;border:4px solid transparent;border-top:5px solid #444}

.post-card{width:302px;height:151px;background:var(--panel)}
.post-card .frame{position:absolute;left:15px;top:18px;width:126px;height:118px;background:var(--white);border:1px solid #ddd;box-shadow:0 1px 3px rgba(0,0,0,.2);padding:4px}
.post-card .frame .ph,.listing .ph{width:100%;height:100%}
.car-title{font-size:13px;font-weight:700;color:var(--link-blue)}
.car-desc{font-size:12px;color:var(--muted);line-height:18px}
.post-card .txt{position:absolute;left:150px;top:44px;width:146px}

.listing{width:282px;height:100px}
.listing .img{position:absolute;left:0;top:0;width:122px;height:100px}
.listing .txt{position:absolute;left:131px;top:6px;width:150px}

.review{left:127px;top:1837px;width:642px;height:378px}
.avatar{position:absolute;left:30px;top:44px;width:176px;height:176px;border-radius:50%;background:var(--white);box-shadow:0 2px 6px rgba(0,0,0,.2);padding:8px}
.avatar .ph{width:100%;height:100%;border-radius:50%}
.review .who{position:absolute;left:20px;width:210px;text-align:center}
.review .body{position:absolute;left:280px;top:254px;width:345px;font-size:15px;color:var(--muted);line-height:28px}

.news{left:789px;width:284px}
.news p{font-size:12px;color:var(--muted);line-height:25px}
.news .date{font-size:13px;font-weight:700;color:var(--link-blue);margin-top:2px;padding-left:4px}

/* footer */
.footer{left:0;top:2249px;width:1200px;height:297px;background:var(--footer)}
.footer h4{font-size:14px;font-weight:700;color:var(--link-blue);margin-bottom:20px}
.footer .col{position:absolute;top:36px}
.footer .col a{display:block;font-size:12px;color:#444;text-decoration:none;line-height:22px}
.footer .note{font-size:12px;color:#555;line-height:21px;width:230px}
.footer .in{width:221px;height:27px;background:var(--white);border:1px solid #ddd;font-size:11px;color:#888;padding:6px 12px;margin-top:10px}
.footer .subscribe{position:absolute;left:124px;top:194px;width:97px;height:24px;background:var(--form-blue);color:var(--white);font-size:12px;font-weight:700;border-radius:12px;display:flex;align-items:center;justify-content:center}
.social{position:absolute;left:0;width:136px;height:30px}
.social .dot{position:absolute;left:0;top:0;width:30px;height:30px;border-radius:50%;background:var(--tab-dark)}
.social span{position:absolute;right:0;top:6px;font-size:13px;color:#444}
.copyright{left:0;top:2493px;width:1200px;text-align:center;font-size:12px;color:#222}
</style>
</head>
<body>

<!-- top bar -->
<div class="abs topbar">
  <div class="abs search">Search
    <svg width="14" height="14" viewBox="0 0 14 14"><circle cx="6" cy="6" r="4.5" fill="none" stroke="#888" stroke-width="1.6"/><line x1="9.3" y1="9.3" x2="13" y2="13" stroke="#888" stroke-width="1.8"/></svg>
  </div>
  <div class="abs auth">SIGN IN &nbsp;|&nbsp; LOGIN</div>
</div>

<!-- header -->
<header class="abs header">
  <div class="abs logo">
    <div class="mark"></div>
    <div class="name">Query Tobin</div>
    <div class="slogan">buying a ride?, selling a ride?, ride a dive? Query Tobin</div>
  </div>
  <nav class="abs nav">
    <a class="active">Buy</a><a>Sell</a><a>News</a><a>Care Tips</a><a>Finance</a><a>Insurance</a><a>FAQ</a>
  </nav>
</header>

<!-- hero -->
<section class="abs hero" role="img" aria-label="Photo of an orange sports coupe driving fast on a mountain road under a cloudy sky">
  <div class="abs tagline">We deal only with used cars</div>
  <div class="abs arrow" style="left:64px;top:209px"><svg width="56" height="56"><polyline points="32,18 22,28 32,38" fill="none" stroke="#333" stroke-width="4"/></svg></div>
  <div class="abs arrow" style="left:1080px;top:209px"><svg width="56" height="56"><polyline points="24,18 34,28 24,38" fill="none" stroke="#333" stroke-width="4"/></svg></div>
  <div class="abs tabs"><div class="tab used">Used</div><div class="tab cpo">Certified Pre-Owned</div></div>
  <form class="abs search-form">
    <div class="field" style="top:27px">All Makes<span class="caret"></span></div>
    <div class="field" style="top:101px">All Models<span class="caret"></span></div>
    <div class="field" style="top:181px">No Maximum Price<span class="caret"></span></div>
    <div class="field miles" style="top:261px">30 miles<span class="caret"></span></div>
    <div class="btn-download">Download</div>
    <div class="links" style="left:28px">or Customize a New Car</div>
    <div class="links" style="left:254px">Advanced Search</div>
  </form>
</section>

<!-- buying used cars -->
<section class="abs panel" style="left:127px;top:727px;width:642px;height:489px">
  <div class="abs panel-title" style="left:27px;top:16px">Buying Used Cars</div>
  <div class="abs pager" style="left:590px;top:12px">‹›</div>
  <div class="thumb" style="left:27px;top:76px"><div class="ph" role="img" aria-label="Red SUV" style="background:linear-gradient(#fff,#c8262a 60%,#eee)"></div></div>
  <div class="cat-label" style="left:30px;top:236px">SUV</div>
  <div class="thumb" style="left:234px;top:76px"><div class="ph" role="img" aria-label="Black pickup truck" style="background:linear-gradient(#fff,#222 60%,#eee)"></div></div>
  <div class="cat-label" style="left:232px;top:236px">PICKUP TRUCKER</div>
  <div class="thumb" style="left:441px;top:76px"><div class="ph" role="img" aria-label="Grey luxury sports car" style="background:linear-gradient(#777,#3a3a3a 60%,#999)"></div></div>
  <div class="cat-label" style="left:439px;top:236px">LUXURY CAR</div>
  <div class="thumb" style="left:27px;top:286px"><div class="ph" role="img" aria-label="Silver sedan" style="background:linear-gradient(#fff,#8d9196 60%,#eee)"></div></div>
  <div class="cat-label" style="left:30px;top:446px">SEDAN</div>
  <div class="thumb" style="left:234px;top:286px"><div class="ph" role="img" aria-label="Red crossover" style="background:linear-gradient(#3a3a3a,#b52424 60%,#555)"></div></div>
  <div class="cat-label" style="left:232px;top:446px">CROSS OVER</div>
  <div class="thumb" style="left:441px;top:286px"><div class="ph" role="img" aria-label="Silver van" style="background:linear-gradient(#fff,#b4b8c0 60%,#eee)"></div></div>
  <div class="cat-label" style="left:439px;top:446px">VAN</div>
</section>

<!-- dealer finder -->
<aside class="abs panel dealer">
  <div class="abs panel-title" style="left:16px;top:14px">Find Dealers Near You</div>
  <div class="abs" style="left:16px;top:42px;font-size:13px;color:#aaa">Get maps, car listings and price quotes:</div>
  <div class="lbl" style="top:70px">Make</div>
  <div class="input" style="top:94px">Ardena<span style="position:absolute;right:8px;top:12px;width:16px;height:15px;border:1px solid #aaa"></span></div>
  <div class="lbl" style="top:153px">ZIP Code</div>
  <div class="input" style="top:168px"></div>
  <div class="abs btn-orange" style="left:19px;top:224px;width:146px;height:33px;font-size:12px">Find a dealer</div>
</aside>
<div class="abs" role="img" aria-label="Advertisement banner showing a silver people carrier in front of city buildings" style="left:789px;top:1024px;width:282px;height:186px;background:linear-gradient(120deg,#c9ccd1,#8b9098 50%,#e5e6e8)"></div>

<!-- posting used cars -->
<h2 class="abs section-head" style="left:129px;top:1254px">POSTING USED CARS</h2>
<div class="abs filter" style="left:127px;top:1310px;width:342px">Car<span class="caret"></span></div>
<div class="abs filter" style="left:485px;top:1310px;width:162px">Price<span class="caret"></span></div>
<div class="abs btn-orange" style="left:658px;top:1310px;width:111px;height:41px;font-size:13px">POST NOW</div>

<div class="abs post-card" style="left:127px;top:1378px">
  <div class="frame"><div class="ph" role="img" aria-label="White sports coupe in a showroom" style="background:linear-gradient(#ddd,#f4f4f4 60%,#aaa)"></div></div>
  <div class="txt"><div class="car-title">2014 Corvane XR Sport</div><div class="car-desc">unde omnis iste natus error sit voluptatem accusantium doloremque</div></div>
</div>
<div class="abs post-card" style="left:470px;top:1378px">
  <div class="frame"><div class="ph" role="img" aria-label="Pink hatchback" style="background:linear-gradient(#555,#c2245e 60%,#333)"></div></div>
  <div class="txt"><div class="car-title">2014 Corvane XR Sport</div><div class="car-desc">unde omnis iste natus error sit voluptatem accusantium doloremque</div></div>
</div>
<div class="abs post-card" style="left:127px;top:1563px">
  <div class="frame"><div class="ph" role="img" aria-label="Red sports car" style="background:linear-gradient(#eee,#c21d1d 60%,#999)"></div></div>
  <div class="txt"><div class="car-title">2014 Corvane XR Sport</div><div class="car-desc">unde omnis iste natus error sit voluptatem accusantium doloremque</div></div>
</div>
<div class="abs post-card" style="left:470px;top:1563px">
  <div class="frame"><div class="ph" role="img" aria-label="Blue sports car" style="background:linear-gradient(#ccc,#1e6bb8 60%,#333)"></div></div>
  <div class="txt"><div class="car-title">2014 Corvane XR Sport</div><div class="car-desc">unde omnis iste natus error sit voluptatem accusantium doloremque</div></div>
</div>

<!-- view used cars -->
<h2 class="abs section-head" style="left:789px;top:1254px">VIEW USED CARS</h2>
<div class="abs pager" style="left:1045px;top:1250px">‹›</div>
<div class="abs listing" style="left:789px;top:1312px">
  <div class="img ph" role="img" aria-label="Blue sedan" style="background:linear-gradient(#eef,#1d4fb0 60%,#ccc)"></div>
  <div class="txt"><div class="car-title">2014 Corvane XR Sport</div><div class="car-desc">unde omnis iste natus error sit voluptatem accusantium doloremque</div></div>
</div>
<div class="abs listing" style="left:789px;top:1465px">
  <div class="img ph" role="img" aria-label="Black SUV" style="background:linear-gradient(#ddd,#1f1f1f 60%,#bbb)"></div>
  <div class="txt"><div class="car-title">2014 Corvane XR Sport</div><div class="car-desc">unde omnis iste natus error sit voluptatem accusantium doloremque</div></div>
</div>
<div class="abs listing" style="left:789px;top:1618px">
  <div class="img ph" role="img" aria-label="Silver SUV" style="background:linear-gradient(#555,#9aa0a6 60%,#444)"></div>
  <div class="txt"><div class="car-title">2014 Corvane XR Sport</div><div class="car-desc">unde omnis iste natus error sit voluptatem accusantium doloremque</div></div>
</div>

<!-- reviews -->
<h2 class="abs section-head" style="left:129px;top:1784px">USED CAR REVIEWS</h2>
<section class="abs panel review">
  <div class="abs pager" style="left:590px;top:14px">‹›</div>
  <div class="avatar"><div class="ph" role="img" aria-label="Portrait of the reviewer" style="background:radial-gradient(circle at 50% 40%,#e2b08f,#c55a3a 70%,#f4f4f4)"></div></div>
  <div class="abs" role="img" aria-label="Silver sedan on a coastal road" style="left:273px;top:46px;width:343px;height:170px;background:linear-gradient(#b9cde0,#d6dde3 45%,#8f969c 70%,#c8c8c8)"></div>
  <div class="who" style="top:262px;font-size:20px;font-weight:600;color:var(--brand-blue)">Marcus Delane</div>
  <div class="who" style="top:288px;font-size:20px;font-weight:600;color:var(--brand-blue)">SEDAN CAR</div>
  <div class="who" style="top:318px;font-size:14px;color:var(--muted)">Bought for $ 15,000</div>
  <div class="body">Lorem Ipsum is simply dummy text of the printing and typesetting industry. Lorem Ipsum has been the industry's standard dummy text ever since the 1500s, when an unknown printer</div>
</section>

<!-- latest news -->
<h2 class="abs section-head" style="left:789px;top:1784px">LATEST NEWS</h2>
<div class="abs news" style="top:1830px"><p>Lorem ipsum dolor sit amet, consectetur adipisicing elit, sed do eiusmod tempor incididunt ut labore et dolore magna aliqua.</p><div class="date">23-11-2013 GST &nbsp;22:10</div></div>
<div class="abs news" style="top:1977px"><p>Lorem ipsum dolor sit amet, consectetur adipisicing elit, sed do eiusmod tempor incididunt ut labore et dolore magna aliqua.</p><div class="date">23-11-2013 GST &nbsp;22:10</div></div>
<div class="abs news" style="top:2124px"><p>Lorem ipsum dolor sit amet, consectetur adipisicing elit, sed do eiusmod tempor incididunt ut labore et dolore magna aliqua.</p><div class="date">23-11-2013 GST &nbsp;22:10</div></div>

<!-- footer -->
<footer class="abs footer">
  <div class="col" style="left:134px"><h4>Quick Links</h4><a>Buy</a><a>Sell</a><a>News</a><a>Care Tips</a><a>Finance</a><a>Insurance</a><a>FAQ</a></div>
  <div class="col" style="left:377px"><h4>Support Links</h4><a>Legal Notice</a><a>Privacy Policy</a><a>Terms &amp; Conditions</a><a>Help</a></div>
  <div class="col" style="left:618px;width:240px;height:230px"><h4>Newsletter SignUp</h4>
    <p class="note">Sign-up for our daily emails by entering your information below:</p>
    <div class="in">Name</div><div class="in">Enter Your E-Mail ID</div>
    <div class="subscribe">Subscribe</div>
  </div>
  <div class="col" style="left:935px;width:136px;height:200px"><h4>Connect With Us</h4>
    <div class="social" style="top:40px"><div class="dot"></div><span>Chirpnet</span></div>
    <div class="social" style="top:77px"><div class="dot"></div><span>Pinloop</span></div>
    <div class="social" style="top:114px"><div class="dot"></div><span>Linkwork</span></div>
  </div>
</footer>
<div class="abs copyright">Copyright ©2013 Company Name &nbsp;- All rights reserved</div>

</body>
</html>
```